Business Card Design - TBW (company name)

Over 20 years of progressive technology design, migration and management experience that drives business objectives and streamlines operations. Continuously challenge conventions to meet and exceed business security, availability and functionality requirements. Maintain exceptional vendor relationships to ensure ongoing knowledge of emerging products and to secure preferred service agreements. Recruit and utilize top talent and foster a collegial environment that advances innovation and performance excellence. design logo using 3 arrows of different colors green, gold, blue

Industry/Entity Type

Progressive

Contact Information for Business Card

Martin K. Osgood
IT Strategist / Consultant

626.583.2904 MOsgood@tbwosgood.com 4817 Ferndale Court Pasadena, CA 91107

Colors
0255a3
f37122
fece3e

Requirements
Must have
• Note NEW EMAIL ADDRESS
• MOsgood@tbwosgood.com
• NOTE NEW ORDER of the work I do.
• Infrastructure – Systems – Cybersecurity
Nice to have
• main color should be orange

```html
<!DOCTYPE html>
<html lang="en">
<head>
<meta charset="utf-8">
<title>TBW Business Card</title>
<link rel="stylesheet" href="https://fonts.googleapis.com/css2?family=Jura:wght@300;400;500;700&family=PT+Sans:wght@700&display=swap">
<style>
  :root {
    --brand-blue: #0255a3;
    --brand-blue-light: #1ba3de;
    --brand-orange: #f37122;
    --brand-orange-light: #f9a533;
    --brand-gold: #fece3e;
    --brand-gold-light: #ffec3a;
    --mark-grey: #c9cacc;
    --ink: #111111;
    --white: #ffffff;
    --edge: #b5b5b5;
  }
  html, body {
    margin: 0;
    padding: 0;
    width: 1013px;
    height: 1200px;
    overflow: hidden;
    background: var(--white);
  }
  .sheet {
    position: relative;
    width: 1013px;
    height: 1200px;
  }
  .card {
    position: absolute;
    left: 43px;
    width: 927px;
    height: 543px;
    display: block;
  }
  .card--front { top: 49px; }
  .card--back { top: 611px; }
  .card-edge { fill: var(--white); stroke: var(--edge); stroke-width: 1.5; }
  .band-gold { fill: url(#goldGlow); }
  .band-blue { fill: url(#blueGlow); }
  .band-orange { fill: url(#orangeGlow); }
  .divider { stroke: var(--white); stroke-width: 1.5; opacity: .8; }
  .mark-dot { fill: var(--mark-grey); }
  .wordmark {
    font-family: "Jura", sans-serif;
    font-weight: 700;
    letter-spacing: 2px;
  }
  .wordmark--front { fill: var(--brand-blue); font-size: 46px; }
  .wordmark--back { fill: var(--white); font-size: 44px; }
  .person-name {
    font-family: "Jura", sans-serif;
    font-weight: 400;
    font-size: 56px;
    fill: var(--white);
  }
  .person-title {
    font-family: "Jura", sans-serif;
    font-weight: 400;
    font-size: 27px;
    fill: var(--white);
  }
  .contact-line {
    font-family: "PT Sans", sans-serif;
    font-weight: 700;
    font-size: 41px;
    fill: var(--white);
  }
  .address-line {
    font-family: "Jura", sans-serif;
    font-weight: 500;
    font-style: italic;
    font-size: 41px;
    fill: var(--ink);
  }
  .service {
    font-family: "Jura", sans-serif;
    font-weight: 500;
    font-size: 44px;
    fill: var(--white);
  }
</style>
</head>
<body>
<main class="sheet">

  <svg class="card card--front" viewBox="0 0 1086 636" aria-label="Business card front">
    <defs>
      <radialGradient id="blueGlow" cx="0.5" cy="0.45" r="0.6">
        <stop offset="0" stop-color="var(--brand-blue-light)"/>
        <stop offset="1" stop-color="var(--brand-blue)"/>
      </radialGradient>
      <radialGradient id="goldGlow" cx="0.45" cy="0.6" r="0.6">
        <stop offset="0" stop-color="var(--brand-gold-light)"/>
        <stop offset="1" stop-color="var(--brand-gold)"/>
      </radialGradient>
      <linearGradient id="orangeGlow" x1="0" y1="0" x2="1" y2="0">
        <stop offset="0" stop-color="var(--brand-orange)"/>
        <stop offset="0.5" stop-color="var(--brand-orange-light)"/>
        <stop offset="1" stop-color="var(--brand-orange)"/>
      </linearGradient>
    </defs>
    <rect class="card-edge" x="0.75" y="0.75" width="1084.5" height="634.5"/>
    <polygon class="band-blue" points="0,210 413,210 478,131 1086,131 1086,520 0,520"/>
    <polygon class="band-gold" points="0,83 515,83 413,210 0,210"/>
    <polygon class="band-orange" points="670,426 1086,426 1086,552 570,552"/>

    <circle class="mark-dot" cx="199" cy="103" r="68"/>
    <text class="wordmark wordmark--front" x="290" y="150">TBW</text>

    <text class="person-name" x="463" y="318" text-anchor="end">Martin K. Osgood</text>
    <text class="person-title" x="288" y="363" text-anchor="middle">IT Strategist / Consultant</text>

    <line class="divider" x1="487" y1="215" x2="487" y2="436"/>

    <text class="contact-line" x="520" y="313">T: 626.583.2904</text>
    <text class="contact-line" x="520" y="373">E: MOsgood@tbwosgood.com</text>

    <text class="address-line" x="668" y="483">4817 Ferndale Court</text>
    <text class="address-line" x="668" y="526">Pasadena CA, 91107</text>
  </svg>

  <svg class="card card--back" viewBox="0 0 1086 636" aria-label="Business card back">
    <defs>
      <radialGradient id="blueGlowBack" cx="0.5" cy="0.5" r="0.62">
        <stop offset="0" stop-color="var(--brand-blue-light)"/>
        <stop offset="1" stop-color="var(--brand-blue)"/>
      </radialGradient>
    </defs>
    <rect x="0" y="0" width="1086" height="636" fill="url(#blueGlowBack)"/>

    <circle class="mark-dot" cx="526" cy="230" r="97"/>
    <text class="wordmark wordmark--back" x="526" y="380" text-anchor="middle">TBW</text>

    <text class="service service-list" x="560" y="455" text-anchor="middle"><tspan>•Infrastructure</tspan><tspan dx="28">•Systems</tspan><tspan dx="28">•Cybersecurity</tspan></text>
  </svg>

</main>
</body>
</html>
```